Postcard Mailer

We are a pizza pub that is the only local restaurant that offers and delivers pizza, burgers, salads and wings.

We just opened and want to send out a postcard to the community. thinking on one side a nice design with pics etc. then on the back a list of our daily food and drink specials.

Industry/Entity Type

Restaurant

Colors
eb1f27

```html
<!DOCTYPE html>
<html lang="en">
<head>
<meta charset="utf-8">
<title>Rosa and Marco – Postcard Mailer</title>
<link href="https://fonts.googleapis.com/css2?family=Archivo+Black&family=Alfa+Slab+One&family=Kalam:wght@400;700&display=swap" rel="stylesheet">
<style>
:root{
  --bg:#eceded;
  --wood-dark:#2b2321;
  --wood-mid:#4a3d38;
  --brand-red:#eb1f27;
  --band-red:#d9262b;
  --open-orange:#f25a22;
  --day-blue:#5ab8e6;
  --ink:#111111;
  --paper:#ffffff;
  --line:#555555;
  --crust:#d9a35a;
  --sauce:#b8432a;
  --title-grey:#d8d8d8;
}
*{margin:0;padding:0;box-sizing:border-box}
html,body{width:1200px;height:1000px;overflow:hidden;background:var(--bg)}
.canvas{position:relative;width:1200px;height:1000px}
.card{position:absolute;left:301px;width:598px;height:463px;overflow:hidden}
.card-front{top:27px;background:linear-gradient(180deg,var(--wood-mid),var(--wood-dark))}
.card-back{top:509px;background:var(--paper)}
.pizza-photo{position:absolute;left:0;top:0;width:598px;height:350px;
  background:radial-gradient(ellipse at 30% 40%,var(--sauce) 0%,var(--crust) 45%,transparent 62%),
             radial-gradient(ellipse at 66% 55%,var(--sauce) 0%,var(--crust) 42%,transparent 58%)}
.brand-box{position:absolute;right:46px;top:0;width:108px;height:110px;background:var(--paper);
  border:1px solid var(--ink);display:flex;flex-direction:column;align-items:center;justify-content:center;gap:4px;text-align:center}
.brand-mark{width:30px;height:30px;border-radius:50%;background:var(--ink)}
.brand-name{font-family:"Archivo Black",sans-serif;font-size:8.5px;color:var(--ink);line-height:1.1}
.brand-info{font-family:"Archivo Black",sans-serif;font-size:6px;color:var(--ink);line-height:1.3}
.headline{position:absolute;left:0;right:0;top:350px;text-align:center;white-space:nowrap;font-weight:normal}
.headline-script{font-family:"Kalam",cursive;font-size:42px;color:var(--paper)}
.headline-bold{font-family:"Archivo Black",sans-serif;font-size:34px;color:var(--open-orange);text-transform:uppercase}
.food-band{position:absolute;left:0;right:0;top:403px;height:45px;background:var(--band-red);
  display:flex;align-items:center;justify-content:center;gap:5px;white-space:nowrap;
  font-family:"Alfa Slab One",serif;font-size:25px;color:var(--paper);letter-spacing:.5px}
.food-band .star{font-size:14px}
.back-specials{position:absolute;left:0;top:0;width:290px;height:463px;background:linear-gradient(180deg,var(--wood-mid),var(--wood-dark))}
.brush-splash{position:absolute;left:20px;top:50px;width:270px;height:400px;background:var(--brand-red);
  border-radius:45% 55% 40% 50% / 30% 40% 60% 70%;opacity:.9}
.menu{position:absolute;left:0;width:290px;top:13px;text-align:center;font-family:"Kalam",cursive;font-weight:700;
  font-size:11.5px;line-height:11px;color:var(--paper);text-transform:uppercase}
.menu-title{font-family:"Alfa Slab One",serif;font-size:14px;line-height:18px;color:var(--title-grey);letter-spacing:1px}
.menu-rule{width:150px;margin:2px auto 4px;border-top:2px dotted var(--title-grey)}
.menu-day{font-family:"Alfa Slab One",serif;font-size:11.5px;line-height:13px;margin-top:2px;color:var(--day-blue);text-transform:none;letter-spacing:.3px}
.menu-day:first-of-type{margin-top:0}
.address-side{position:absolute;left:290px;top:0;width:308px;height:463px}
.back-brand{position:absolute;left:14px;top:18px;width:90px;text-align:center;display:flex;flex-direction:column;align-items:center;gap:4px}
.back-brand .brand-mark{width:40px;height:40px}
.postage{position:absolute;left:196px;top:28px;width:87px;height:96px;border:1px solid var(--line);
  font-family:Arial,sans-serif;font-size:10px;text-align:center;padding-top:30px;line-height:1.3;color:#222}
.address-line{position:absolute;left:21px;width:233px;border-top:1px solid var(--line)}
</style>
</head>
<body>
<div class="canvas">
  <section class="card card-front">
    <div class="pizza-photo" role="img" aria-label="Photo of two pizzas, a supreme and a pepperoni, on a dark wood table"></div>
    <div class="brand-box">
      <span class="brand-mark"></span>
      <span class="brand-name">ROSA AND MARCO</span>
      <span class="brand-info">HARBORVIEW, NC<br>555.014.0188</span>
    </div>
    <h1 class="headline"><span class="headline-script">Come in, </span><span class="headline-bold">We’re open</span></h1>
    <div class="food-band"><span class="star">★</span>PIZZA<span class="star">★</span>BURGERS<span class="star">★</span>SALADS<span class="star">★</span>WINGS</div>
  </section>

  <section class="card card-back">
    <div class="back-specials">
      <div class="brush-splash" role="img" aria-label="Red brush stroke decoration"></div>
      <div class="menu">
        <div class="menu-title">MENU SPECIALS</div>
        <div class="menu-rule"></div>
        <div class="menu-day">Daily Lunch Special</div>
        <div>2 slices + drink $4.95</div>
        <div class="menu-day">Monday</div>
        <div>Buy 1 medium pizza get 1 free</div>
        <div>$1 domestic beers</div>
        <div class="menu-day">Tuesday</div>
        <div>Medium pizza $7.95</div>
        <div>50 cent wings</div>
        <div>$1.50 drafts</div>
        <div class="menu-day">Wednesday</div>
        <div>Classic burger + beer $5.95</div>
        <div>$2.50 Ember shots</div>
        <div class="menu-day">Thursday</div>
        <div>$1 slice night</div>
        <div>$2.50 craft beers</div>
        <div class="menu-day">Friday</div>
        <div>2 medium pizzas $15.95</div>
        <div>$2 glasses of wine</div>
        <div class="menu-day">Saturday</div>
        <div>1/2 price salads</div>
        <div>$3 vodka drinks</div>
        <div>$2.50 Pine Ridge Amber</div>
        <div class="menu-day">Sunday</div>
        <div>Large pizza $9.95</div>
        <div>$3 Bloody Mary’s &amp; Mimosa’s</div>
        <div class="menu-rule" style="margin-top:6px"></div>
      </div>
    </div>
    <div class="address-side">
      <div class="back-brand">
        <span class="brand-mark"></span>
        <span class="brand-name">ROSA AND MARCO</span>
        <span class="brand-info">HARBORVIEW, NC<br>555.014.0188</span>
      </div>
      <div class="postage">Postage<br>Area</div>
      <div class="address-line" style="top:229px"></div>
      <div class="address-line" style="top:259px"></div>
      <div class="address-line" style="top:290px"></div>
      <div class="address-line" style="top:321px"></div>
      <div class="address-line" style="top:352px"></div>
    </div>
  </section>
</div>
</body>
</html>
```